PELDIVUX HOA Portal Site for Public

Clean up and organize current website; need website to look good and functional; this is a HOA (homeowner association management) website where homeowners can login and pay their bill, general information about a HOA, monthly newsletter page.
Competitors:
https://lumaridge.example/
https://bexolirnada.example/
https://www.qvhabitations.example/nevada
http://www.tpq-hoa.example/

Target Market(s)

homeowners

Industry/Entity Type

Real Estate

Coding

Coded - Design and coding required

Number of Pages Required

5+ page

Font styles to use
Serif

Colors
0292cd
33a6d7
e667a6
e34297

Requirements
Must have
• login to pay
• services page
• contact us
• order resale package
Nice to have
• page why an HOA would contract us

```html
<!DOCTYPE html>
<html lang="en">
<head>
<meta charset="utf-8">
<title>PELDIVUX HOA</title>
<link href="https://fonts.googleapis.com/css2?family=Merriweather:wght@400;700&family=Montserrat:wght@800&family=Nunito+Sans:wght@400;600;700&display=swap" rel="stylesheet">
<style>
:root{
  --blue:#0292cd;
  --blue-soft:#33a6d7;
  --pink:#e34297;
  --pink-soft:#e667a6;
  --ink:#222;
  --grey:#666;
  --white:#fff;
}
*{box-sizing:border-box;margin:0;padding:0}
html,body{width:1200px;height:3620px;overflow:hidden}
body{font-family:"Nunito Sans",sans-serif;color:var(--ink);position:relative;background:var(--white)}
section,header,footer{position:relative;width:1200px}
.btn{display:inline-block;font-family:"Merriweather",serif;font-size:19px;color:var(--white);padding:0 24px;line-height:52px;height:52px}
.btn-pink{background:var(--pink)}
.btn-blue{background:var(--blue)}

.topbar{height:42px;background:var(--blue);display:flex;align-items:center;padding:0 88px 0 78px;color:var(--white);font-size:15px}
.social{display:flex;gap:5px}
.social span{width:30px;height:30px;border-radius:50%;background:var(--blue-soft);display:block}
.social span:first-child{background:var(--pink)}
.topbar-links{margin-left:auto;display:flex;gap:30px;align-items:center}
.topbar-links div{display:flex;align-items:center;gap:8px}

.site-head{height:135px;text-align:center}
.logo{font-family:"Merriweather",serif;font-weight:700;color:var(--blue);font-size:31px;padding-top:24px}
.nav{display:flex;justify-content:center;margin-top:28px;font-size:14.5px;font-weight:700;letter-spacing:.3px}
.nav a{padding:0 20px;border-left:1px solid #ccc;color:#222;text-decoration:none;line-height:18px}
.nav a:first-child{border:none;color:var(--pink)}

.hero{height:500px;background:linear-gradient(100deg,#3a2c26 0%,#6b3a2e 35%,#8a5746 55%,#4d4a45 80%,#2f3a2e 100%)}
.hero-inner{position:absolute;left:75px;top:87px;color:var(--white)}
.hero h1{font-family:"Montserrat",sans-serif;font-weight:800;font-size:46px;line-height:52px;letter-spacing:.5px}
.hero p{font-size:15px;line-height:26px;margin-top:12px;width:400px}
.hero .btns{margin-top:22px;display:flex;gap:7px}
.dots{position:absolute;right:32px;top:189px;display:flex;flex-direction:column;gap:8px}
.dots span{width:15px;height:15px;border-radius:50%;border:1.5px solid var(--white)}
.dots span.on{background:var(--pink);border-color:var(--pink)}

.pay-band{height:93px;background:var(--pink);display:flex;align-items:center;justify-content:center;gap:24px;color:var(--white)}
.pay-band h2{font-family:"Merriweather",serif;font-weight:400;font-size:23px}
.pay-band .outline{border:1.5px solid var(--white);font-family:"Merriweather",serif;font-size:19px;line-height:50px;padding:0 24px}

.about{height:490px;text-align:center;padding-top:55px}
.about h2{font-family:"Merriweather",serif;color:var(--blue);font-size:42px;font-weight:400}
.about .lead{font-weight:700;font-size:16px;line-height:27px;margin-top:24px}
.about .body{color:var(--grey);font-size:14px;line-height:27px;width:580px;margin:14px auto 0}
.about .btn{margin-top:26px}

.services{height:542px;background:var(--blue);color:var(--white);text-align:center;overflow:hidden}
.services h2{font-family:"Merriweather",serif;font-size:42px;font-weight:400;padding-top:55px}
.services .sub{font-size:16px;margin-top:12px}
.services-photo{position:absolute;left:405px;top:180px;width:390px;height:362px;background:linear-gradient(160deg,rgba(224,187,133,.55),rgba(199,154,94,.55))}
.svc{position:absolute;top:235px;width:300px}
.svc h3{font-family:"Merriweather",serif;font-size:17px;line-height:27px;font-weight:700}
.svc p{font-size:15px;line-height:27px;margin-top:20px}
.svc-left{left:0;text-align:right}
.svc-left h3,.svc-left p{margin-left:100px}
.svc-right{left:912px;text-align:left}
.svc-right h3{width:230px}
.svc-right p{width:200px}
.svc-icon{position:absolute;top:230px;width:88px;height:88px;border-radius:50%;background:var(--pink);border:3px solid var(--white);display:flex;align-items:center;justify-content:center}
.arrow{margin-top:12px}

.offer{height:573px;background:linear-gradient(100deg,#0f2540 0%,#1e3a5c 45%,#3a5677 75%,#2a3d55 100%)}
.offer-inner{position:absolute;left:76px;top:52px;width:490px;color:#e8eef5}
.offer h2{font-family:"Merriweather",serif;color:var(--blue);font-size:42px;font-weight:700}
.offer ul{list-style:none;font-size:14.5px;line-height:31px;margin-top:18px}
.offer p{font-size:14.5px;line-height:26px;margin-top:12px}
.offer .btn{margin-top:18px}

.testimonial{height:427px;background:var(--blue);text-align:center;color:var(--white)}
.testimonial h2{font-family:"Merriweather",serif;font-weight:400;font-size:42px;padding-top:55px}
.quote-mark{width:66px;height:66px;border-radius:50%;background:var(--pink);border:3px solid var(--white);margin:28px auto 0;display:flex;align-items:center;justify-content:center}
.testimonial p{width:640px;margin:30px auto 0;font-size:15px;line-height:27px}
.testimonial .name{font-family:"Merriweather",serif;font-size:19px;margin-top:20px}

.newsletter{height:368px;text-align:center}
.newsletter h2{font-family:"Merriweather",serif;font-weight:400;color:var(--blue);font-size:42px;line-height:52px;padding-top:55px}
.newsletter .sub{font-size:16px;margin-top:16px}
.signup{width:804px;height:86px;margin:24px auto 0;border-top:1.5px solid #444;border-bottom:1.5px solid #444;display:flex;align-items:center;padding:0 12px 0 7px}
.signup .field{width:574px;height:52px;background:#eee;text-align:left;padding-left:14px;line-height:52px;font-size:14px;color:#777}
.signup .divider{width:1.5px;height:86px;background:#444;margin:0 10px}
.signup .btn{padding:0 36px}

.site-foot{height:347px;background:linear-gradient(180deg,#23272f,#1a1e24 60%,#22272a);text-align:center;color:#ddd}
.site-foot .logo{padding-top:50px;font-size:38px}
.site-foot .social{justify-content:center;margin-top:18px;gap:4px}
.site-foot .social span{width:44px;height:44px;background:#30343b}
.site-foot .social span:first-child{background:var(--pink)}
.contacts{display:flex;justify-content:center;gap:30px;margin-top:58px;font-size:14.5px;text-align:left;line-height:24px}
.contacts .item{display:flex;gap:14px;align-items:center}
.contacts .ring{width:48px;height:48px;border-radius:50%;border:1.5px solid var(--pink);display:flex;align-items:center;justify-content:center;flex:none}
.contacts small{font-size:13px;display:block}

.legal{position:absolute;top:3517px;height:103px;width:1200px;background:var(--pink);color:var(--white);text-align:center;font-size:13.5px;padding-top:22px;line-height:30px}
.legal a{color:var(--white);text-decoration:none;padding:0 8px}
</style>
</head>
<body>

<div class="topbar">
  <div class="social" aria-label="Social links"><span></span><span></span><span></span><span></span></div>
  <div class="topbar-links">
    <div><svg width="16" height="16" viewBox="0 0 24 24"><path d="M6.6 10.8a15 15 0 0 0 6.6 6.6l2.2-2.2c.3-.3.7-.4 1-.2 1.1.4 2.3.6 3.6.6.6 0 1 .4 1 1V20c0 .6-.4 1-1 1A17 17 0 0 1 3 4c0-.6.4-1 1-1h3.5c.6 0 1 .4 1 1 0 1.3.2 2.5.6 3.6.1.3 0 .7-.2 1z" fill="var(--pink)"/></svg>123 456 7890</div>
    <div><svg width="14" height="14" viewBox="0 0 24 24"><circle cx="10" cy="10" r="7" stroke="#fff" stroke-width="3" fill="none"/><path d="M15 15l6 6" stroke="#fff" stroke-width="3"/></svg>Search</div>
    <div><svg width="14" height="14" viewBox="0 0 24 24"><circle cx="12" cy="7" r="5" fill="#fff"/><path d="M3 23c0-6 4-9 9-9s9 3 9 9z" fill="#fff"/></svg>Login</div>
  </div>
</div>

<header class="site-head">
  <div class="logo">PELDIVUX HOA</div>
  <nav class="nav">
    <a>HOME</a><a>SERVICES</a><a>ORDER RESALE PACKAGE</a><a>WHY HOA CONTRACT US</a><a>CONTACT US</a>
  </nav>
</header>

<section class="hero" role="img" aria-label="Family of three facing a red brick house">
  <div class="hero-inner">
    <h1>HOMEOWNER<br>ASSOCIATION<br>MANAGEMENT</h1>
    <p>Lorem Ipsum is simply dummy text of the printing and typesetting industry Ipsum has&nbsp; industry.</p>
    <div class="btns"><span class="btn btn-pink">CONTACT US</span><span class="btn btn-blue">LOGIN</span></div>
  </div>
  <div class="dots"><span></span><span></span><span class="on"></span><span></span><span></span></div>
</section>

<section class="pay-band">
  <h2>Login To Pay Your Bill With PELDIVUX HOA</h2>
  <span class="outline">LOGIN</span>
</section>

<section class="about">
  <h2>About Peldivux Hoa</h2>
  <p class="lead">Lorem Ipsum is simply dummy text of the printing and typesetting industry.<br>Lorem Ipsum has been the industry's standard dummy.</p>
  <p class="body">Lorem Ipsum is simply dummy text of the printing and typesetting industry. Lorem Ipsum has been the industry's standard dummy text ever since the 1500s, when an unknown printer took a galley of type and scrambled it to make a type specimen book. printer took a galley of type and.</p>
  <p class="body" style="margin-top:8px">Lorem Ipsum is simply dummy text of the printing and typesetting industry.</p>
  <span class="btn btn-pink">LEARN MORE</span>
</section>

<section class="services">
  <h2>HOA Provide Best Services</h2>
  <p class="sub">Lorem Ipsum is simply dummy text of the printing and typesetting industry type text.</p>
  <div class="services-photo" role="img" aria-label="Photo of a wooden homeowners association sign"></div>

  <div class="svc svc-left">
    <h3>Association<br>Management Services</h3>
    <p>Lorem Ipsum is simply<br>dummy text of the printing<br>and typesetting industry<br>type text.</p>
    <svg class="arrow" width="36" height="12" viewBox="0 0 36 12" style="margin-right:4px"><path d="M35 6H2M7 1L2 6l5 5" stroke="#fff" stroke-width="1.5" fill="none"/></svg>
  </div>
  <div class="svc-icon" style="left:324px">
    <svg width="50" height="50" viewBox="0 0 50 50" fill="none" stroke="#fff" stroke-width="2"><circle cx="25" cy="18" r="8"/><circle cx="25" cy="18" r="3"/><path d="M6 30l8 10h10M44 30l-8 10H26"/></svg>
  </div>

  <div class="svc-icon" style="left:802px">
    <svg width="50" height="50" viewBox="0 0 50 50" fill="none" stroke="#fff" stroke-width="2"><rect x="13" y="22" width="24" height="16"/><path d="M8 42h34M25 38v4"/><circle cx="10" cy="12" r="3"/><circle cx="25" cy="10" r="3"/><circle cx="40" cy="12" r="3"/></svg>
  </div>
  <div class="svc svc-right">
    <h3>Peldivux Manages Communities Throughout Southern Nevada</h3>
    <p>Lorem Ipsum is simply dummy text of the printing and typesetting industry type text.</p>
    <svg class="arrow" width="36" height="12" viewBox="0 0 36 12"><path d="M1 6h33M29 1l5 5-5 5" stroke="#fff" stroke-width="1.5" fill="none"/></svg>
  </div>
</section>

<section class="offer" role="img" aria-label="Couple embracing in front of a modern house at dusk">
  <div class="offer-inner">
    <h2>What We Offer</h2>
    <ul>
      <li>Accessible, licensed Association Managers</li>
      <li>24 hour Web site access: online account information</li>
      <li>24 hour emergency service</li>
      <li>Provide monthly financial reports to the Board of Directors</li>
    </ul>
    <p>Read, study and understand all governing documents of the Association. Correspond with members in violation of the CC&amp;Rs, By-laws, Rules &amp; Regulations and report the status of all noncompliance to the Board of Directors in a timely manner.</p>
    <p>Act as the custodian of the corporate records. Coordinate preparing annual tax returns for the Association.</p>
    <span class="btn btn-pink">LEARN MORE</span>
  </div>
</section>

<section class="testimonial">
  <h2>What Our Client Say About Us</h2>
  <div class="quote-mark"><svg width="28" height="22" viewBox="0 0 28 22" fill="#fff"><path d="M0 22V12C0 5 4 1 11 0v4C7 5 5 8 5 11h6v11zM16 22V12c0-7 4-11 11-12v4c-4 1-6 4-6 7h6v11z"/></svg></div>
  <p>" Lorem Ipsum is simply dummy text of the printing and typesetting industry. Lorem Ipsum has been the industry's standard dummy Lorem Ipsum is simply dummy text of the printing typesetting industry.</p>
  <div class="name">— Client Name</div>
</section>

<section class="newsletter">
  <h2>Join Our Newsletter<br>Subscription</h2>
  <p class="sub">Would you like to Receive our Exclusive News and update for sign up Our Newsletter !</p>
  <div class="signup">
    <div class="field">Enter Email *</div>
    <div class="divider"></div>
    <span class="btn btn-pink">SUBSCRIBE</span>
  </div>
</section>

<footer class="site-foot" role="img" aria-label="Dark residential street at night">
  <div class="logo">PELDIVUX HOA</div>
  <div class="social"><span></span><span></span><span></span><span></span></div>
  <div class="contacts">
    <div class="item"><span class="ring"><svg width="18" height="22" viewBox="0 0 18 22"><path d="M9 1a8 8 0 0 0-8 8c0 6 8 12 8 12s8-6 8-12a8 8 0 0 0-8-8z" fill="none" stroke="var(--pink)" stroke-width="2"/><circle cx="9" cy="9" r="3" fill="var(--pink)"/></svg></span><div>101 - Address city location,<br>Area, Pincode, Zip...</div></div>
    <div class="item"><span class="ring"><svg width="20" height="20" viewBox="0 0 24 24"><path d="M6.6 10.8a15 15 0 0 0 6.6 6.6l2.2-2.2c.3-.3.7-.4 1-.2 1.1.4 2.3.6 3.6.6.6 0 1 .4 1 1V20c0 .6-.4 1-1 1A17 17 0 0 1 3 4c0-.6.4-1 1-1h3.5c.6 0 1 .4 1 1 0 1.3.2 2.5.6 3.6.1.3 0 .7-.2 1z" fill="var(--pink)"/></svg></span><div><small>Phone :</small>123 456 7890</div></div>
    <div class="item"><span class="ring"><svg width="20" height="16" viewBox="0 0 20 16"><rect x="1" y="1" width="18" height="14" rx="2" fill="var(--pink)"/><path d="M1 2l9 7 9-7" stroke="#1e2228" stroke-width="1.5" fill="none"/></svg></span><div><small>Email :</small>info@PeldivuxHOA.example</div></div>
  </div>
</footer>

<div class="legal">
  <div><a>HOME</a>|<a>SERVICES</a>|<a>ORDER RESALE PACKAGE</a>|<a>WHY HOA CONTRACT US</a>|<a>CONTACT US</a></div>
  <div>©PELDIVUX HOA - 2019 All rights reserved.</div>
</div>

</body>
</html>
```